Velorin business card design

Design a business card for a cryptocurrency company that uses the attached logo. Some example business cards to give you guys a flavor of what we're looking for is given below (of course feel free to be creative):
https://www.plumcardhub.example/studio.aspx?template=4819265_KT3&ag=True&xnav=HSG_Design_Image&rd=1
https://www.plumcardhub.example/studio.aspx?template=3027514_KT3&ag=True&xnav=HSG_Design_Image&rd=1
The business card should be clean/simple and convey the company name, what we're about and the specific persons contact info. In terms of what we're about, we can have our name Velorin, with a line under it that says "Cryptocurrency visualization, analytics, and trading"
We want something futuristic looking but simple / clean.
The color scheme for the logo should be used.
The name of the person and their title should be editable, so we can use the business card design for multiple people.
(Please use the zip file to get the vector graphics and different image formats)

```html
<!DOCTYPE html>
<html lang="en">
<head>
<meta charset="utf-8">
<title>Velorin business card</title>
<link rel="stylesheet" href="https://fonts.googleapis.com/css2?family=Roboto:wght@400;500;700&family=Roboto+Condensed:wght@400&display=swap">
<style>
  :root {
    --stage: #818181;
    --navy: #15253a;
    --navy-text: #1a2a3d;
    --white: #ffffff;
    --mark-faint: #f3f3f3;
    --blue: #0a7cc4;
    --teal: #0a9fb2;
    --green: #6dc28a;
  }
  * { box-sizing: border-box; margin: 0; padding: 0; }
  html, body { width: 1200px; height: 996px; overflow: hidden; }
  body { background: var(--stage); position: relative; font-family: "Roboto", sans-serif; }

  .card { position: absolute; left: 339px; width: 521px; height: 322px; overflow: hidden; }
  .card--front { top: 156px; background: var(--navy); }
  .card--back { top: 518px; background: var(--white); }

  .front-pattern {
    position: absolute; inset: 0;
    background: radial-gradient(circle at 50% 50%, rgba(255,255,255,0.03), rgba(255,255,255,0.015));
  }
  .front-brand {
    position: absolute; left: 0; right: 0; top: 128px;
    display: flex; align-items: center; justify-content: center; gap: 12px;
  }
  .brand-square { width: 40px; height: 40px; background: var(--teal); }
  .brand-name {
    font-family: "Roboto", sans-serif; font-weight: 500; font-size: 44px;
    letter-spacing: 3px; line-height: 1; color: var(--white);
  }
  .front-tagline {
    position: absolute; left: 0; right: 0; top: 187px; text-align: center;
    font-family: "Roboto Condensed", sans-serif; font-size: 15px; color: var(--white);
  }

  .back-mark-area {
    position: absolute; left: 301px; top: 14px; width: 220px; height: 244px;
    background: linear-gradient(90deg, rgba(243,243,243,0.6), var(--mark-faint));
  }
  .back-brand {
    position: absolute; left: 42px; top: 130px;
    display: flex; align-items: center; gap: 10px;
  }
  .back-brand .brand-square { width: 38px; height: 38px; }
  .back-brand .brand-name { color: var(--navy-text); font-size: 40px; letter-spacing: 2px; }

  .person { position: absolute; left: 300px; top: 89px; color: var(--navy-text); }
  .person-name { font-weight: 700; font-size: 21px; line-height: 1.2; }
  .person-title { font-size: 13.5px; margin-top: 2px; }

  .contacts { position: absolute; left: 300px; top: 158px; list-style: none; }
  .contacts li {
    display: flex; align-items: center; gap: 8px; height: 19.5px;
    font-size: 13px; color: var(--navy-text);
  }
  .contacts svg { width: 14px; height: 14px; flex: none; }

  .tag-band { position: absolute; left: 0; bottom: 0; width: 521px; height: 47px; }
  .back-tagline {
    position: absolute; left: 230px; bottom: 18px;
    font-family: "Roboto Condensed", sans-serif; font-size: 13.5px; color: var(--white);
  }
</style>
</head>
<body>
  <section class="card card--front">
    <div class="front-pattern" role="img" aria-label="Faint repeating brand-mark pattern across the card"></div>
    <div class="front-brand">
      <span class="brand-square"></span>
      <span class="brand-name">VELORIN</span>
    </div>
    <p class="front-tagline">Cryptocurrency Visualization, Analytics and Trading</p>
  </section>

  <section class="card card--back">
    <div class="back-mark-area" role="img" aria-label="Large faint brand mark decoration"></div>
    <div class="back-brand">
      <span class="brand-square"></span>
      <span class="brand-name">VELORIN</span>
    </div>

    <div class="person">
      <h1 class="person-name">Arin Talwar</h1>
      <p class="person-title">Founder &amp; Product Architect</p>
    </div>

    <ul class="contacts">
      <li>
        <svg viewBox="0 0 14 14"><polygon points="7,0.5 12.8,3.8 12.8,10.2 7,13.5 1.2,10.2 1.2,3.8" fill="var(--teal)"/><path d="M4.2 8.5h5.6v1.3H4.2zM5 6.2h4l0.8 2.3H4.2z" fill="#fff"/></svg>
        <span>646-318-2095</span>
      </li>
      <li>
        <svg viewBox="0 0 14 14"><polygon points="7,0.5 12.8,3.8 12.8,10.2 7,13.5 1.2,10.2 1.2,3.8" fill="var(--teal)"/><rect x="3.8" y="4.8" width="6.4" height="4.4" fill="none" stroke="#fff" stroke-width="0.9"/><path d="M3.8 4.8L7 7.4l3.2-2.6" fill="none" stroke="#fff" stroke-width="0.9"/></svg>
        <span>arin.talwar@velorin.com</span>
      </li>
      <li>
        <svg viewBox="0 0 14 14"><polygon points="7,0.5 12.8,3.8 12.8,10.2 7,13.5 1.2,10.2 1.2,3.8" fill="var(--blue)"/><circle cx="7" cy="7" r="3" fill="none" stroke="#fff" stroke-width="0.8"/><path d="M4 7h6M7 4v6" stroke="#fff" stroke-width="0.7"/></svg>
        <span>www.velorin.com</span>
      </li>
    </ul>

    <svg class="tag-band" viewBox="0 0 521 47" preserveAspectRatio="none">
      <defs>
        <linearGradient id="stripeGrad" x1="0" x2="1" y1="0" y2="0">
          <stop offset="0" stop-color="var(--blue)"/>
          <stop offset="0.5" stop-color="var(--teal)"/>
          <stop offset="1" stop-color="var(--green)"/>
        </linearGradient>
      </defs>
      <rect x="0" y="25" width="200" height="22" fill="url(#stripeGrad)"/>
      <path d="M189 47 L210 8 Q214 0 224 0 L521 0 L521 47 Z" fill="var(--navy)"/>
    </svg>
    <p class="back-tagline">Cryptocurrency Visualization, Analytics and Trading</p>
  </section>
</body>
</html>
```